We are seeking two label designs for our premium pecan snack brand, MORVELO. MORVELO is known for its innovative pecan snacks, specifically a healthy and exotic blend of pecans, expertly salted, and infused with unique chili flavors. Our snacks are packaged in stand-up pouch bags, and we are looking for label designs product sizes - 5 oz. ( Size: 14 x 20 cm / 5.5 x 7.8 inches / Max Capacity: 16.2 oz)

Background Information:
MORVELO is a brand committed to offering a delightful snacking experience that combines the natural richness of pecans with the bold and exotic kick of carefully selected chilies. Our snacks cater to health-conscious consumers who appreciate the fusion of premium quality, unique flavors, and nutritional goodness.

Target Market(s)

Event Attendees (Entertainment Industry), Health-Conscious Consumers

Industry/Entity Type

Entertainment (sports events, arenas, stadiums, etc)

Font styles to use
Other font styles liked:
• Brother1816 Printed

Colors

Designer to choose colors to be used in the design.

Requirements
Must have
• Nutrition Fact (attached) , TRANSPARENT PART LIKE A WINDOW TO DISPLAY THE PRODUCT

```html
<!DOCTYPE html>
<html lang="en">
<head>
<meta charset="utf-8">
<title>MORVELO Pouch Labels</title>
<link rel="stylesheet" href="https://fonts.googleapis.com/css2?family=Oswald:wght@500;600&family=Raleway:wght@400;500;700;800&display=swap">
<style>
  :root {
    --stage: #f6ee78;
    --pouch: #141414;
    --pouch-soft: #232317;
    --accent: #f2dc1d;
    --logo: #ececec;
    --ink: #141414;
    --panel: #ffffff;
    --nut-light: #c99a5e;
    --nut-dark: #7a4f26;
  }
  html, body {
    margin: 0;
    padding: 0;
    width: 1200px;
    height: 966px;
    overflow: hidden;
    background: var(--stage);
  }
  .canvas {
    position: relative;
    width: 1200px;
    height: 966px;
  }

  /* label base */
  .label {
    position: absolute;
    overflow: hidden;
    background: var(--pouch);
  }
  .label--small { left: 330px; top: 400px; width: 250px; height: 380px; }
  .label--large { left: 620px; top: 260px; width: 340px; height: 520px; }

  .label__pattern {
    position: absolute;
    inset: 0;
    background: linear-gradient(160deg, var(--pouch) 0%, var(--pouch-soft) 50%, var(--pouch) 100%);
  }

  .label__flavour-band {
    position: absolute;
    top: 0;
    background: var(--accent);
    display: flex;
    align-items: center;
    justify-content: center;
  }
  .label__flavour {
    margin: 0;
    font-family: "Oswald", sans-serif;
    font-weight: 600;
    line-height: 1.1;
    text-align: center;
    text-transform: uppercase;
    color: var(--ink);
  }

  .label__rule {
    position: absolute;
    left: 0;
    right: 0;
    background: var(--accent);
  }

  .label__brand {
    position: absolute;
    left: 0;
    right: 0;
    display: flex;
    flex-direction: column;
    align-items: center;
    justify-content: center;
  }
  .brand__name {
    font-family: "Raleway", sans-serif;
    font-weight: 500;
    color: var(--logo);
    line-height: 1;
  }
  .brand__maker {
    align-self: flex-end;
    font-family: "Raleway", sans-serif;
    font-weight: 500;
    letter-spacing: 0.05em;
    color: var(--logo);
    text-transform: uppercase;
  }

  .label__window {
    position: absolute;
    border: 2px solid var(--accent);
    border-radius: 16px;
    background: radial-gradient(circle at 40% 40%, var(--nut-light) 0%, var(--nut-dark) 100%);
  }

  .label__weight-band {
    position: absolute;
    bottom: 0;
    background: var(--accent);
    display: flex;
    align-items: center;
    justify-content: center;
  }
  .label__weight {
    font-family: "Oswald", sans-serif;
    font-weight: 600;
    color: var(--ink);
    letter-spacing: 0.04em;
  }

  /* small label sizes */
  .label--small .label__flavour-band { left: 86px; width: 92px; height: 78px; }
  .label--small .label__flavour { font-size: 15px; }
  .label--small .label__rule--top { top: 124px; height: 4px; }
  .label--small .label__brand { top: 132px; height: 52px; }
  .label--small .brand__name { font-size: 25px; letter-spacing: 2px; }
  .label--small .brand__maker { font-size: 6px; margin: 4px 44px 0 0; }
  .label--small .label__rule--bottom { top: 188px; height: 4px; }
  .label--small .label__window { left: 55px; top: 212px; width: 136px; height: 128px; }
  .label--small .label__weight-band { left: 66px; width: 118px; height: 20px; }
  .label--small .label__weight { font-size: 10px; }

  /* large label sizes */
  .label--large .label__flavour-band { left: 112px; width: 126px; height: 106px; }
  .label--large .label__flavour { font-size: 21px; }
  .label--large .label__rule--top { top: 168px; height: 5px; }
  .label--large .label__brand { top: 178px; height: 72px; }
  .label--large .brand__name { font-size: 34px; letter-spacing: 3px; }
  .label--large .brand__maker { font-size: 8px; margin: 6px 64px 0 0; }
  .label--large .label__rule--bottom { top: 256px; height: 5px; }
  .label--large .label__window { left: 22px; top: 282px; width: 140px; height: 190px; }
  .label--large .label__weight-band { left: 90px; width: 160px; height: 24px; }
  .label--large .label__weight { font-size: 12px; }

  /* nutrition facts */
  .nutrition {
    position: absolute;
    left: 178px;
    top: 282px;
    width: 140px;
    box-sizing: border-box;
    padding: 5px 6px;
    background: var(--panel);
    color: var(--ink);
    font-family: "Raleway", sans-serif;
    font-size: 7.5px;
    line-height: 1.35;
  }
  .nutrition__title {
    margin: 0;
    font-weight: 800;
    font-size: 14px;
    line-height: 1.05;
    border-bottom: 1px solid var(--ink);
    padding-bottom: 2px;
  }
  .nutrition__serving {
    margin: 2px 0 0;
    border-bottom: 4px solid var(--ink);
    padding-bottom: 2px;
  }
  .nutrition__calories {
    display: flex;
    justify-content: space-between;
    font-weight: 800;
    font-size: 11px;
    border-bottom: 2px solid var(--ink);
    padding: 1px 0;
  }
  .nutrition__table {
    width: 100%;
    border-collapse: collapse;
  }
  .nutrition__table td {
    border-bottom: 1px solid var(--ink);
    padding: 1px 0;
  }
  .nutrition__table td:last-child { text-align: right; font-weight: 700; }
  .nutrition__table .nutrient { font-weight: 700; }
  .nutrition__table .sub { padding-left: 8px; }
</style>
</head>
<body>
<main class="canvas">
  <section class="label label--small">
    <div class="label__pattern" role="img" aria-label="Scattered yellow chili pepper pattern on black"></div>
    <div class="label__flavour-band"><p class="label__flavour">Salted<br>Exotic<br>Flavour</p></div>
    <div class="label__rule label__rule--top"></div>
    <div class="label__brand">
      <span class="brand__name">MORVELO</span>
      <span class="brand__maker">By Trenova</span>
    </div>
    <div class="label__rule label__rule--bottom"></div>
    <div class="label__window" role="img" aria-label="Clear window showing the salted chili pecans inside"></div>
    <div class="label__weight-band"><span class="label__weight">NET WT 5 OZ</span></div>
  </section>

  <section class="label label--large">
    <div class="label__pattern" role="img" aria-label="Scattered yellow chili pepper pattern on black"></div>
    <div class="label__flavour-band"><p class="label__flavour">Salted<br>Exotic<br>Flavour</p></div>
    <div class="label__rule label__rule--top"></div>
    <div class="label__brand">
      <span class="brand__name">MORVELO</span>
      <span class="brand__maker">By Trenova</span>
    </div>
    <div class="label__rule label__rule--bottom"></div>
    <div class="label__window" role="img" aria-label="Clear window showing the salted chili pecans inside"></div>
    <div class="nutrition">
      <p class="nutrition__title">Nutrition Facts</p>
      <p class="nutrition__serving">About 5 servings per pouch<br><b>Serving size 1 oz (28g)</b></p>
      <div class="nutrition__calories"><span>Calories</span><span>200</span></div>
      <table class="nutrition__table">
        <tr><td class="nutrient">Total Fat 20g</td><td>26%</td></tr>
        <tr><td class="sub">Saturated Fat 2g</td><td>10%</td></tr>
        <tr><td class="nutrient">Sodium 120mg</td><td>5%</td></tr>
        <tr><td class="nutrient">Total Carb. 4g</td><td>1%</td></tr>
        <tr><td class="sub">Dietary Fiber 3g</td><td>11%</td></tr>
        <tr><td class="sub">Total Sugars 1g</td><td></td></tr>
        <tr><td class="nutrient">Protein 3g</td><td></td></tr>
      </table>
    </div>
    <div class="label__weight-band"><span class="label__weight">NET WT 5 OZ (142g)</span></div>
  </section>
</main>
</body>
</html>
```